Design door hanger Bonaire Diving

We would like to have a design for a door hanger (See example below).
One side: Promote reef taster diving.
Other side: Promote Unlimited air/nitrox packages - lowest price guaranteed on Bonaire

We would like to inform people who rent a car with us about our air packages for diving. And non divers should be triggered to come and do a Reef Taster Dive with us. (KT Car rental and KT Dive is the same company.)

Target Market(s)

Divers and potential divers

Industry/Entity Type

Diving industry

Font styles to use
Sans Serif

Colors
0054AA
0677BA
7BADD7
CADEEF
E8F1F8
EE7325
F08F49
F5BC92
FAE3D3
FDF4ED

Requirements
Must have
• a few of the pictures included

```html
<!DOCTYPE html>
<html lang="en">
<head>
<meta charset="utf-8">
<title>KT Dive door hangers</title>
<link rel="stylesheet" href="https://fonts.googleapis.com/css2?family=Poppins:wght@400;500;600;700;800;900&family=Oswald:wght@500;600;700&display=swap">
<style>
  :root {
    --backdrop: #c6c6c6;
    --ocean-light: #2f67b0;
    --ocean-mid: #1c4a93;
    --ocean-deep: #0c2c66;
    --ocean-dark: #0a1f45;
    --amber: #e8950f;
    --sky: #6db2e6;
    --sky-pale: #a9d2f2;
    --white: #ffffff;
    --ink: #10233f;
    --panel: rgba(40, 90, 170, 0.55);
  }
  * { box-sizing: border-box; margin: 0; padding: 0; }
  html, body { width: 1200px; height: 900px; overflow: hidden; }
  body {
    background: var(--backdrop);
    font-family: "Poppins", sans-serif;
    position: relative;
  }
  .hanger {
    position: absolute;
    top: 176px;
    width: 222px;
    height: 576px;
    color: var(--white);
  }
  .hanger--taster { left: 222px; }
  .hanger--air { left: 643px; }
  .hanger__shape { position: absolute; inset: 0; width: 222px; height: 576px; }
  .hanger > *:not(.hanger__shape) { position: absolute; left: 0; right: 0; text-align: center; white-space: nowrap; }

  .brand { top: 176px; font-weight: 700; font-size: 17px; line-height: 18px; color: var(--white); }
  .dots { display: flex; justify-content: center; gap: 2px; }
  .dots span { width: 5px; height: 5px; border-radius: 50%; border: 1px solid var(--sky-pale); }
  .dots span:last-child { background: var(--sky); border-color: var(--sky); }

  /* taster side */
  .headline-main { top: 256px; font-weight: 800; font-size: 29px; line-height: 34px; letter-spacing: -0.5px; }
  .headline-sub { top: 288px; font-weight: 800; font-size: 22px; line-height: 26px; }
  .headline-sub .accent { color: var(--amber); }
  .headline-sub .cool { color: var(--sky); }
  .hanger--taster .dots { top: 315px; }
  .hanger > .intro { top: 324px; left: 24px; right: 24px; font-size: 7px; line-height: 8.6px; white-space: normal; }
  .hanger > .perks {
    top: 366px; left: 16px; right: 14px; height: 121px;
    background: var(--panel); border-radius: 10px; list-style: none;
    padding: 9px 6px 0 9px; text-align: left; white-space: normal;
  }
  .perks li { display: flex; gap: 3px; font-size: 6.6px; line-height: 8px; font-weight: 500; margin-bottom: 8px; }
  .perks svg { flex: none; width: 8px; height: 8px; }

  /* air side */
  .hanger--air .headline-main { top: 253px; font-size: 30px; }
  .headline-air { top: 283px; font-weight: 800; font-size: 19px; line-height: 22px; color: var(--amber); }
  .hanger > .rate-band { top: 305px; left: 18px; right: 18px; height: 18px; }
  .rate-band span { position: relative; font-weight: 700; font-size: 10px; letter-spacing: 1.8px; color: var(--ocean-deep); line-height: 18px; }
  .rate-band svg { position: absolute; inset: 0; width: 100%; height: 100%; }
  .hanger--air .dots { top: 327px; }
  .hanger > .offer-box {
    top: 341px; left: 40px; right: 41px; height: 39px;
    background: var(--panel); border-radius: 8px; padding-top: 6px;
  }
  .offer-box .offer-top { font-weight: 700; font-size: 12.5px; line-height: 13px; }
  .offer-box .offer-top em { font-style: normal; color: var(--amber); }
  .offer-box .offer-bottom { font-weight: 500; font-size: 10.5px; letter-spacing: 2px; line-height: 13px; }
  .nitrox-label { top: 387px; font-weight: 500; font-size: 7.6px; letter-spacing: 1.8px; }
  .nitrox-place { top: 391px; font-weight: 800; font-size: 25px; line-height: 32px; color: var(--amber); }
  .hanger > .psi-box {
    top: 433px; left: 28px; right: 31px; height: 55px;
    border: 1px solid rgba(255,255,255,0.75); border-radius: 9px;
    display: flex; align-items: center; padding-left: 8px;
  }
  .psi-box .fill-note { width: 42px; flex: none; text-align: right; font-weight: 700; font-size: 8.5px; line-height: 10px; padding-right: 4px; border-right: 1px solid rgba(255,255,255,0.7); }
  .psi-box .psi { text-align: left; padding-left: 5px; font-family: "Oswald", sans-serif; white-space: nowrap; }
  .psi-box .psi-value { font-weight: 600; font-size: 27px; line-height: 30px; color: var(--amber); }
  .psi-box .psi-note { font-weight: 500; font-size: 8.5px; line-height: 11px; }
  .psi-box .psi-note span { color: var(--sky); }

  /* shared footer */
  .site { top: 514px; font-weight: 600; font-size: 10px; letter-spacing: 1px; color: var(--ocean-deep); line-height: 14px; }
  .hanger > .call { top: 535px; font-weight: 700; font-size: 12px; color: var(--ink); display: flex; justify-content: center; align-items: center; gap: 3px; }
  .call svg { width: 12px; height: 12px; }
</style>
</head>
<body>

<section class="hanger hanger--taster">
  <svg class="hanger__shape" viewBox="0 0 222 576" role="img" aria-label="Underwater photo of divers, a sea turtle and coral reef in deep blue tones">
    <defs>
      <clipPath id="shape-taster">
        <path d="M0,108 A111,108 0 0 1 222,108 L222,540 Q222,576 186,576 L36,576 Q0,576 0,540 Z"/>
      </clipPath>
      <linearGradient id="sea-taster" x1="0" y1="0" x2="0" y2="1">
        <stop offset="0" stop-color="#2f67b0"/>
        <stop offset="0.45" stop-color="#1c4a93"/>
        <stop offset="1" stop-color="#0c2c66"/>
      </linearGradient>
    </defs>
    <g clip-path="url(#shape-taster)">
      <rect width="222" height="576" fill="url(#sea-taster)"/>
      <path d="M0,530 Q111,508 222,530 L222,576 L0,576 Z" fill="var(--amber)"/>
      <path d="M35,524 L46,512 L178,512 L190,524 L178,531 L46,531 Z" fill="#4a90c9"/>
      <rect x="45" y="510" width="134" height="21" rx="5" fill="var(--sky)"/>
    </g>
    <circle cx="111" cy="103" r="52" fill="var(--backdrop)"/>
    <path d="M0,180 Q36,176 70,140 L86,150 Q50,198 0,206 Z" fill="var(--backdrop)"/>
  </svg>

  <div class="brand">KT Car rental<br>&amp; Dive</div>
  <h1 class="headline-main">REEF TASTER</h1>
  <h2 class="headline-sub"><span class="accent">SCUBA</span> <span class="cool">DIVING</span></h2>
  <div class="dots"><span></span><span></span><span></span></div>
  <p class="intro">Dive for the first time and enjoy our underwater paradise to the fullest under the guidance of an instructor. Give yourself a lifetime gift</p>
  <ul class="perks">
    <li><svg viewBox="0 0 8 8"><rect x="0.5" y="0.5" width="7" height="7" rx="1" fill="none" stroke="#fff"/><path d="M1.8,4 L3.4,5.6 L6.4,2" fill="none" stroke="#fff" stroke-width="1.2"/></svg>Ages 10 and up can sign up for our reef taster dive</li>
    <li><svg viewBox="0 0 8 8"><rect x="0.5" y="0.5" width="7" height="7" rx="1" fill="none" stroke="#fff"/><path d="M1.8,4 L3.4,5.6 L6.4,2" fill="none" stroke="#fff" stroke-width="1.2"/></svg>The Reef Taster Diving course will take 3-4 hours</li>
    <li><svg viewBox="0 0 8 8"><rect x="0.5" y="0.5" width="7" height="7" rx="1" fill="none" stroke="#fff"/><path d="M1.8,4 L3.4,5.6 L6.4,2" fill="none" stroke="#fff" stroke-width="1.2"/></svg>A group consists of a maximum of 4 people</li>
    <li><svg viewBox="0 0 8 8"><rect x="0.5" y="0.5" width="7" height="7" rx="1" fill="none" stroke="#fff"/><path d="M1.8,4 L3.4,5.6 L6.4,2" fill="none" stroke="#fff" stroke-width="1.2"/></svg>Experience the splendor of the ocean without much distraction by other divers</li>
    <li><svg viewBox="0 0 8 8"><rect x="0.5" y="0.5" width="7" height="7" rx="1" fill="none" stroke="#fff"/><path d="M1.8,4 L3.4,5.6 L6.4,2" fill="none" stroke="#fff" stroke-width="1.2"/></svg>Enjoy a lot of personal attention given by your instructor</li>
  </ul>
  <div class="site">www.kt-dive.com</div>
  <div class="call">Call us:
    <svg viewBox="0 0 12 12"><circle cx="6" cy="6" r="6" fill="#fff"/><path d="M3.6,3 Q3,3.6 3.4,5 Q4.4,7.6 7,8.6 Q8.4,9 9,8.4 L8,7.2 L7,7.6 Q5.4,6.8 4.6,5.2 L5,4.2 Z" fill="var(--amber)"/></svg>
    (+599) 555 24 60</div>
</section>

<section class="hanger hanger--air">
  <svg class="hanger__shape" viewBox="0 0 222 576" role="img" aria-label="Underwater photo of divers above a dark coral reef in deep blue tones">
    <defs>
      <clipPath id="shape-air">
        <path d="M0,108 A111,108 0 0 1 222,108 L222,540 Q222,576 186,576 L36,576 Q0,576 0,540 Z"/>
      </clipPath>
      <linearGradient id="sea-air" x1="0" y1="0" x2="0" y2="1">
        <stop offset="0" stop-color="#2f67b0"/>
        <stop offset="0.4" stop-color="#1a4590"/>
        <stop offset="0.7" stop-color="#0f2f62"/>
        <stop offset="1" stop-color="#0a1f45"/>
      </linearGradient>
    </defs>
    <g clip-path="url(#shape-air)">
      <rect width="222" height="576" fill="url(#sea-air)"/>
      <path d="M0,530 Q111,508 222,530 L222,576 L0,576 Z" fill="var(--amber)"/>
      <path d="M35,524 L46,512 L178,512 L190,524 L178,531 L46,531 Z" fill="#4a90c9"/>
      <rect x="45" y="510" width="134" height="21" rx="5" fill="var(--sky)"/>
    </g>
    <circle cx="111" cy="103" r="52" fill="var(--backdrop)"/>
    <path d="M0,180 Q36,176 70,140 L86,150 Q50,198 0,206 Z" fill="var(--backdrop)"/>
  </svg>

  <div class="brand">KT Car rental<br>&amp; Dive</div>
  <h1 class="headline-main">UNLIMITED</h1>
  <h2 class="headline-air">SUSTAINABLE AIR</h2>
  <div class="rate-band">
    <svg viewBox="0 0 186 18" preserveAspectRatio="none"><path d="M4,0 L186,0 L182,18 L0,18 Z" fill="var(--sky)"/></svg>
    <span>AT A COMPETITIVE RATE</span>
  </div>
  <div class="dots"><span></span><span></span><span></span></div>
  <div class="offer-box">
    <div class="offer-top">KT Dive <em>OFFERS</em></div>
    <div class="offer-bottom">UNLIMITED AIR</div>
  </div>
  <div class="nitrox-label">NITROX FOR THE LOWEST PRICE</div>
  <div class="nitrox-place">ON BONAIRE</div>
  <div class="psi-box">
    <div class="fill-note">WE FILL<br>YOUR<br>TANK<br>UP TO</div>
    <div class="psi">
      <div class="psi-value">3200 PSI</div>
      <div class="psi-note"><span>220 BAR</span> WITHOUT PROBLEM</div>
    </div>
  </div>
  <div class="site">www.kt-dive.com</div>
  <div class="call">Call us:
    <svg viewBox="0 0 12 12"><circle cx="6" cy="6" r="6" fill="#fff"/><path d="M3.6,3 Q3,3.6 3.4,5 Q4.4,7.6 7,8.6 Q8.4,9 9,8.4 L8,7.2 L7,7.6 Q5.4,6.8 4.6,5.2 L5,4.2 Z" fill="var(--amber)"/></svg>
    (+599) 555 24 60</div>
</section>

</body>
</html>
```